Pirelnuvo.Com - Mobile Top Up

It is the top up site for mobile operators.

Works for 3 mobile operators; Zentrale, Mavibar, Dogru Hatnet
This site will broadcast in Turkish and English for this reason we want to select the language button.
This site will usually serve for Turkey.
Required Pages;

Home page
Payment Page
Communication Page
About Us

We need a colorful and responsive design. Customer reviews, recharge form, and some information should be included at the homepage.

The payment page should include a credit card payment form and customer information.

We want eye-pleasing designs, innovative and easy to use.
Updates

Dear designers :) Please do not make similar designs to our current design !. We started this contest because we wanted a different design. Logic and design will be a mobile top-up site. You can look at it, but please do not do the same!

Target Market(s)

Top up Website

Logo Text

PirelNuvo

Coding

Coded - Design and coding required

Number of Pages Required

4 page

Font styles to use
Serif

Colors
6b449b
e24096
33a6d7
abd036
fbf289
f68d4d
f04a50
d3a5cc

Requirements
Must have
• Payment , contact form, fast payment form , top up form
Nice to have
• look our current design : pirelnuvo.com - we want responsive design

```html
<!DOCTYPE html>
<html lang="en">
<head>
<meta charset="utf-8">
<title>PirelNuvo – Payment Information</title>
<link href="https://fonts.googleapis.com/css2?family=Nunito+Sans:wght@400;600;700&display=swap" rel="stylesheet">
<style>
:root{
  --blue:#33a6d7;
  --green:#abd036;
  --red:#f04a50;
  --pink:#c93f9e;
  --text:#555;
  --label:#666;
  --line:#cfcfcf;
  --field:#f4f4f4;
  --white:#fff;
}
*{box-sizing:border-box;margin:0;padding:0}
html,body{width:1082px;height:1200px;overflow:hidden;background:var(--white);font-family:"Nunito Sans",sans-serif;color:var(--text)}
.page{position:relative;width:1082px;height:1200px}
.site-header{position:absolute;left:0;top:0;width:100%;height:101px;border-bottom:1px solid #d8d8d8}
.brand{position:absolute;left:112px;top:32px;display:flex;align-items:center;gap:8px;font-size:26px;font-weight:700;color:var(--blue)}
.brand-dot{width:18px;height:18px;border-radius:50%;background:var(--green)}
.lang{position:absolute;right:109px;top:10px;display:flex;align-items:center;gap:8px;font-size:12px;color:#777}
.flag{width:32px;height:20px}
.flag-tr{background:#e30a17}
.flag-en{background:#1f2e6b}
.main-nav{position:absolute;right:102px;top:44px;display:flex;gap:26px;font-size:17px;color:#888}
.page-title{position:absolute;left:114px;top:146px;font-size:30px;font-weight:400;color:var(--blue)}
.page-lead{position:absolute;left:114px;top:193px;font-size:16px;color:#444}
.payment-box{position:absolute;left:115px;top:240px;width:852px;height:591px;border:1px solid var(--line)}
.row{position:absolute;left:0;width:100%;height:29px;display:flex;align-items:center}
.row label{width:172px;text-align:right;font-size:14px;color:var(--label)}
.field{position:absolute;left:193px;top:0;width:242px;height:29px;border:1px solid #c9c9c9;background:var(--field);font-size:12px;color:#999;padding-left:12px;display:flex;align-items:center}
.field.short{width:124px}
.select-arrow{position:absolute;right:16px;top:10px}
.cards-row .radio{position:absolute;left:191px;top:9px;width:12px;height:12px;border-radius:50%;border:1px solid #bbb}
.card-badges{position:absolute;left:216px;top:3px;display:flex;gap:11px}
.badge{width:30px;height:20px;border-radius:2px;background:#eee;border:1px solid #ddd}
.badge.b1{border-bottom:3px solid #f4a21c}
.badge.b3{border-bottom:3px solid #f68d4d}
.badge.b4{background:#7ba7cf}
.submit{position:absolute;left:193px;top:521px;width:108px;height:36px;border:none;background:linear-gradient(#f25a5f,var(--red));color:var(--white);font-family:inherit;font-size:14px;font-weight:600;letter-spacing:.5px}
.site-footer{position:absolute;left:0;top:866px;width:100%;height:334px;background:var(--green);color:var(--white)}
.col{position:absolute;top:52px}
.col h3{font-size:18px;font-weight:600;margin-bottom:18px}
.col ul{list-style:none}
.col li{font-size:13.5px;height:29px}
.contact-item{position:relative;padding-left:36px;font-size:13.5px;line-height:19px;margin-bottom:10px}
.contact-item svg{position:absolute;left:0;top:-2px}
.news-form{display:flex;width:277px;height:35px}
.news-input{flex:1;background:var(--white);color:#555;font-size:12px;padding-left:12px;display:flex;align-items:center}
.news-btn{width:94px;background:var(--pink);font-size:14px;font-weight:700;display:flex;align-items:center;justify-content:center}
.socials{display:flex;gap:2px;margin-top:16px}
.social{width:30px;height:30px;border-radius:50%;border:1.5px solid var(--white)}
.pay-row{display:flex;gap:13px;margin-top:14px}
.pay-row .badge{width:34px;height:23px;background:#f3f3f3;border-color:#e2e2e2}
.pay-row .b4{background:#7ba7cf}
.footer-rule{position:absolute;left:107px;top:281px;width:873px;height:1px;background:rgba(255,255,255,.7)}
.copyright{position:absolute;left:0;top:300px;width:100%;text-align:center;font-size:13px}
</style>
</head>
<body>
<div class="page">
  <header class="site-header">
    <div class="brand"><span class="brand-dot"></span>PirelNuvo</div>
    <div class="lang">Select Language
      <span class="flag flag-tr" role="img" aria-label="Turkish language flag"></span>
      <span class="flag flag-en" role="img" aria-label="English language flag"></span>
    </div>
    <nav class="main-nav">
      <span>Home</span><span>Dealership</span><span>Prices</span><span>About Us</span><span>Contact</span><span>Customer Reviews</span>
    </nav>
  </header>

  <h1 class="page-title">Payment Information</h1>
  <p class="page-lead">Please enter your credit card information below and click submit</p>

  <section class="payment-box">
    <div class="row cards-row" style="top:32px"><label>Credit Cards Accepted</label>
      <span class="radio"></span>
      <div class="card-badges">
        <span class="badge b1"></span><span class="badge"></span><span class="badge b3"></span><span class="badge b4"></span><span class="badge"></span>
      </div>
    </div>
    <div class="row" style="top:69px"><label>Card Number</label><span class="field"></span></div>
    <div class="row" style="top:107px"><label>Expiry Date (MM)</label><span class="field short">02/2016</span></div>
    <div class="row" style="top:144px"><label>CVV</label><span class="field short"></span></div>
    <div class="row" style="top:181px"><label>Name on Card</label><span class="field">Select
      <svg class="select-arrow" width="8" height="6" viewBox="0 0 8 6"><path d="M1 1l3 3 3-3" stroke="#555" stroke-width="1.4" fill="none"/></svg></span></div>
    <div class="row" style="top:219px"><label>Country</label><span class="field"></span></div>
    <div class="row" style="top:255px"><label>Address 1</label><span class="field"></span></div>
    <div class="row" style="top:292px"><label>Address 2</label><span class="field"></span></div>
    <div class="row" style="top:329px"><label>City</label><span class="field"></span></div>
    <div class="row" style="top:366px"><label>State</label><span class="field"></span></div>
    <div class="row" style="top:405px"><label>Postal Code</label><span class="field"></span></div>
    <div class="row" style="top:442px"><label>Contact Phone Number</label><span class="field"></span></div>
    <div class="row" style="top:479px"><label>Email address</label><span class="field"></span></div>
    <button class="submit">SUBMIT</button>
  </section>

  <footer class="site-footer">
    <div class="col" style="left:103px">
      <h3>COMPANY</h3>
      <ul><li>About us</li><li>News</li><li>Career Opportunities</li><li>FAQ</li></ul>
    </div>
    <div class="col" style="left:279px">
      <h3>RESOURCES</h3>
      <ul><li>Support</li><li>Sitemap</li><li>Term of Use</li><li>Contact Us</li></ul>
    </div>
    <div class="col" style="left:429px">
      <h3>CONTACT US</h3>
      <div class="contact-item">
        <svg width="28" height="28" viewBox="0 0 28 28"><circle cx="14" cy="14" r="13" fill="none" stroke="#fff" stroke-width="1.5"/><path d="M14 7a4.5 4.5 0 0 0-4.5 4.5c0 3.5 4.5 8.5 4.5 8.5s4.5-5 4.5-8.5A4.5 4.5 0 0 0 14 7z" fill="#fff"/><circle cx="14" cy="11.5" r="1.7" fill="#abd036"/></svg>
        418 Orchard Quay Suite B12<br>Millbrook, PA 19320
      </div>
      <div class="contact-item" style="margin-top:8px">
        <svg width="28" height="28" viewBox="0 0 28 28"><circle cx="14" cy="14" r="13" fill="none" stroke="#fff" stroke-width="1.5"/><path d="M10 8l2.5 2.8-1.2 1.8c.9 1.8 2.3 3.2 4.1 4.1l1.8-1.2L20 18l-1.5 2c-5 0-10.5-5.5-10.5-10.5z" fill="#fff"/></svg>
        +44 (0) 7000 418233
      </div>
      <div class="contact-item" style="margin-top:8px">
        <svg width="28" height="28" viewBox="0 0 28 28"><circle cx="14" cy="14" r="13" fill="none" stroke="#fff" stroke-width="1.5"/><rect x="8" y="10" width="12" height="9" rx="1" fill="#fff"/><path d="M8.5 10.5l5.5 4 5.5-4" stroke="#abd036" stroke-width="1.2" fill="none"/></svg>
        info@pirelnuvo.com
      </div>
    </div>
    <div class="col" style="left:703px">
      <h3>NEWSLETTER SIGN UP</h3>
      <div class="news-form"><span class="news-input">Email address</span><span class="news-btn">SIGN UP</span></div>
      <div class="socials"><span class="social"></span><span class="social"></span><span class="social"></span><span class="social"></span></div>
      <div class="pay-row"><span class="badge"></span><span class="badge"></span><span class="badge"></span><span class="badge b4"></span><span class="badge"></span></div>
    </div>
    <div class="footer-rule"></div>
    <p class="copyright">© 2017 PirelNuvo&nbsp; All right reserved&nbsp; Term of Use</p>
  </footer>
</div>
</body>
</html>
```